New Record Label needs a Web design

We are Iron Heron: a London based, new & independent music production company aimed at the 25-40 age group. The musical style is Soul/Classic Brelvane.
We have at the moment just one signed artist, but will expand in the future.
We dont' have any webpage yet and are looking for an innovative web design for our webpage www.iron-heron-example.com
I have uploaded our company logo.

Initially the whole website will only have 3 tabs: Home page/Artists/Contact

The design should be classic and high-end, but can be a bit crazy too.

```html
<!DOCTYPE html>
<html lang="en">
<head>
<meta charset="utf-8">
<title>Iron Heron — Music Production</title>
<link rel="stylesheet" href="https://fonts.googleapis.com/css2?family=Bebas+Neue&family=Montserrat:wght@400;600;700&display=swap">
<style>
:root{
  --red:#e2322f;
  --orange:#ea772f;
  --ink:#111111;
  --coal:#1b1b1b;
  --panel:#161616;
  --slate:#3c3c3c;
  --white:#ffffff;
  --muted:#c9c9c9;
  --heading:"Bebas Neue", Impact, sans-serif;
  --body:"Montserrat", Arial, sans-serif;
}
*{margin:0;padding:0;box-sizing:border-box}
html,body{width:1200px;height:2941px;overflow:hidden;background:var(--ink)}
.page{position:relative;width:1200px;height:2941px;font-family:var(--body);color:var(--white)}
.abs{position:absolute}
.photo{position:absolute;display:block}

/* header */
.masthead{left:0;top:0;width:1200px;height:327px;background:#121212}
.hero-band{left:0;top:327px;width:1200px;height:667px;background:var(--red)}
.mic-left{left:20px;top:30px;width:150px;height:260px;border-radius:70px 70px 10px 10px;background:radial-gradient(circle at 50% 30%,#d8e2ea,#5d6770 55%,#1a1a1a)}
.mic-right{left:1030px;top:30px;width:150px;height:260px;border-radius:70px 70px 10px 10px;background:radial-gradient(circle at 50% 30%,#d8e2ea,#5d6770 55%,#1a1a1a)}
.crowd{left:180px;top:43px;width:842px;height:363px;background:linear-gradient(180deg,#9a9a9a 0%,#4a4a4a 45%,#1d1d1d 100%);clip-path:polygon(0 8%,50% 0,100% 8%,100% 100%,0 100%)}
.brand-disc{left:467px;top:230px;width:266px;height:266px;border-radius:50%;background:var(--ink);display:flex;align-items:center;justify-content:center;flex-direction:column}
.brand-disc .dot{width:18px;height:18px;border-radius:50%;background:var(--red);margin-bottom:10px}
.brand-disc .name{font-family:var(--heading);font-size:34px;letter-spacing:1px;color:var(--red)}
.main-nav{left:180px;top:406px;width:842px;height:90px;background:var(--ink);display:flex}
.main-nav a{flex:1;display:flex;align-items:center;justify-content:center;font-family:var(--heading);font-size:46px;color:var(--white);text-decoration:none;position:relative;z-index:2}

.welcome{left:182px;top:564px;font-family:var(--heading);line-height:.86;color:var(--ink);font-weight:400}
.welcome span{display:block}
.welcome .w1{font-size:90px}
.welcome .w2{font-size:108px}
.welcome .w3{font-size:136px;color:var(--white)}
.welcome .w4{font-size:68px}
.hero-video{left:494px;top:571px;width:528px;height:360px;background:linear-gradient(135deg,#3a1347 0%,#8a3aa0 45%,#e0a6c9 75%,#4a1a3d 100%)}
.play{position:absolute;border-radius:50%;border:5px solid var(--white);background:rgba(255,255,255,.15)}
.play svg{position:absolute;inset:0;margin:auto}

/* featured videos */
.videos-band{left:0;top:994px;width:1200px;height:781px;background:var(--coal)}
.videos-intro{left:0;top:994px;width:488px;height:781px;background:var(--panel);border-right:2px solid #2a2a2a}
.intro-mark{left:182px;top:1060px;width:285px;display:flex;align-items:center;justify-content:center;gap:10px}
.intro-mark .sq{width:16px;height:16px;background:var(--white)}
.intro-mark .name{font-family:var(--heading);font-size:30px;color:var(--white)}
.videos-title{left:182px;top:1180px;font-family:var(--heading);line-height:.95;font-weight:400}
.videos-title .t1{display:block;font-size:86px;color:var(--white)}
.videos-title .t2{display:block;font-size:112px;color:var(--red)}
.videos-copy{left:182px;top:1388px;width:285px;font-size:20px;line-height:29.5px;color:var(--muted)}
.view-all{left:0;top:1702px;width:488px;height:69px;background:var(--orange);display:flex;align-items:center;justify-content:center;font-family:var(--heading);font-size:34px;color:var(--white);text-decoration:none}
.thumb{left:533px;width:447px;height:206px;box-shadow:0 14px 20px rgba(0,0,0,.6)}
.thumb-1{top:1057px;background:linear-gradient(120deg,#2a0f4a,#7a2fa3 50%,#1d0d2a)}
.thumb-2{top:1282px;background:linear-gradient(120deg,#6d5a4e,#b69b86 50%,#3e332c)}
.thumb-3{top:1514px;background:linear-gradient(120deg,#2c2523,#8a6a58 50%,#c8a48c)}

/* featured artists */
.gap-band{left:0;top:1775px;width:1200px;height:49px;background:#1f1f1f}
.artists-band{left:0;top:1824px;width:1200px;height:362px;background:#050505}
.artists-title{left:0;top:1862px;width:1200px;text-align:center;font-family:var(--heading);font-size:44px;font-weight:400}
.artists-title em{font-style:normal;color:var(--red)}
.artist-card{top:1937px;width:204px;height:148px;border-bottom:6px solid var(--orange)}
.ac-1{left:180px;background:linear-gradient(160deg,#cfcfcf,#3a3a3a)}
.ac-2{left:390px;background:linear-gradient(160deg,#6a6a6a,#111)}
.ac-3{left:602px;background:linear-gradient(160deg,#9a9a9a,#2d2d2d)}
.ac-4{left:814px;background:linear-gradient(160deg,#5d7a8c,#a48566 60%,#2d3a44);border-bottom:none}
.artist-caption{left:814px;top:2085px;width:204px;height:52px;background:var(--orange);padding:9px 12px}
.artist-caption b{display:block;font-size:11px;font-weight:700;letter-spacing:.5px}
.artist-caption small{display:block;font-size:9px;letter-spacing:.5px}
.artist-caption .go{position:absolute;right:10px;top:15px;width:20px;height:20px;border-radius:50%;background:#3a2a20}
.arrow{top:2000px}

/* news + location */
.news-band{left:0;top:2186px;width:1200px;height:609px;background:var(--slate)}
.news-title{left:180px;top:2236px;font-family:var(--heading);font-size:42px;color:var(--red);font-weight:400}
.news-pager{left:580px;top:2250px}
.news-body{left:182px;top:2322px;width:446px;display:flex;flex-direction:column;align-items:flex-start}
.news-headline{font-size:19px;font-weight:700;line-height:31px;letter-spacing:-.2px}
.news-date{margin-top:14px;font-size:14px;color:var(--muted)}
.news-copy{margin-top:22px;font-size:13.5px;line-height:25.8px;color:#d0d0d0}
.read-more{margin-top:26px;width:137px;height:46px;background:#1c1c1c;display:flex;align-items:center;justify-content:center;font-size:14px;font-weight:700;color:var(--white);text-decoration:none}
.location-head{left:639px;top:2186px;width:379px;height:95px;background:var(--red);padding:36px 0 0 26px;font-family:var(--heading);font-size:32px;font-weight:400}
.map{left:639px;top:2281px;width:379px;height:514px;background:linear-gradient(135deg,#e6e6e6,#cfcfcf)}

/* footer */
.site-footer{left:0;top:2795px;width:1200px;height:146px;background:#1e1e1e}
.social{left:0;top:2820px;width:1200px;display:flex;justify-content:center;gap:6px}
.social span{width:23px;height:23px;border-radius:50%;background:#3a3a3a}
.footer-nav{left:0;top:2860px;width:1200px;text-align:center;font-size:11px;font-weight:700}
.footer-nav a{color:var(--white);text-decoration:none;margin:0 14px}
.copyright{left:0;top:2896px;width:1200px;text-align:center;font-size:11px;font-weight:700}
</style>
</head>
<body>
<div class="page">

  <header>
    <div class="abs masthead"></div>
    <div class="abs hero-band"></div>
    <div class="photo mic-left" role="img" aria-label="Chrome vintage studio microphone"></div>
    <div class="photo mic-right" role="img" aria-label="Chrome vintage studio microphone"></div>
    <div class="photo crowd" role="img" aria-label="Black and white concert crowd with raised hands under stage lights"></div>
    <nav class="abs main-nav">
      <a href="#">HOME</a><a href="#">ARTISTS</a><a href="#">CONTACT</a>
    </nav>
    <div class="abs brand-disc"><span class="dot"></span><span class="name">Iron Heron</span></div>
  </header>

  <section>
    <h1 class="abs welcome"><span class="w1">WELCOME</span><span class="w2">TO OUR</span><span class="w3">MUSIC</span><span class="w4">PRODUCTION</span></h1>
    <div class="photo hero-video" role="img" aria-label="Video still of a singer at a microphone under purple stage light">
      <span class="play" style="left:214px;top:130px;width:96px;height:96px"><svg width="40" height="44" viewBox="0 0 40 44"><path d="M6 2 L38 22 L6 42 Z" fill="#fff"/></svg></span>
    </div>
  </section>

  <section>
    <div class="abs videos-band"></div>
    <div class="abs videos-intro"></div>
    <div class="abs intro-mark"><span class="sq"></span><span class="name">Iron Heron</span></div>
    <h2 class="abs videos-title"><span class="t1">FEATURED</span><span class="t2">VIDEOS</span></h2>
    <p class="abs videos-copy">At vero eos et accusamus et iusto odio dignissimos ducimus qui blanditiis praesentium voluptatum deleniti atque corrupti quos dolores et quas molestias excepturi sint occaecati cupiditate non provident, similique sunt</p>
    <a class="abs view-all" href="#">VIEW ALL</a>
    <div class="photo thumb thumb-1" role="img" aria-label="Video still of a guitarist silhouetted in purple light">
      <span class="play" style="left:191px;top:71px;width:64px;height:64px"><svg width="26" height="30" viewBox="0 0 40 44"><path d="M6 2 L38 22 L6 42 Z" fill="#fff"/></svg></span>
    </div>
    <div class="photo thumb thumb-2" role="img" aria-label="Video still of hands playing a guitar fretboard">
      <span class="play" style="left:191px;top:71px;width:64px;height:64px"><svg width="26" height="30" viewBox="0 0 40 44"><path d="M6 2 L38 22 L6 42 Z" fill="#fff"/></svg></span>
    </div>
    <div class="photo thumb thumb-3" role="img" aria-label="Video still of a vocalist singing into a studio microphone">
      <span class="play" style="left:191px;top:71px;width:64px;height:64px"><svg width="26" height="30" viewBox="0 0 40 44"><path d="M6 2 L38 22 L6 42 Z" fill="#fff"/></svg></span>
    </div>
  </section>

  <section>
    <div class="abs gap-band"></div>
    <div class="abs artists-band"></div>
    <h2 class="abs artists-title">FEATURED <em>ARTISTS</em></h2>
    <svg class="abs arrow" style="left:148px" width="14" height="24" viewBox="0 0 14 24"><path d="M12 2 L2 12 L12 22" fill="none" stroke="#777" stroke-width="3"/></svg>
    <svg class="abs arrow" style="left:1038px" width="14" height="24" viewBox="0 0 14 24"><path d="M2 2 L12 12 L2 22" fill="none" stroke="#777" stroke-width="3"/></svg>
    <div class="photo artist-card ac-1" role="img" aria-label="Black and white photo of a violinist performing"></div>
    <div class="photo artist-card ac-2" role="img" aria-label="Black and white photo of a singer on stage"></div>
    <div class="photo artist-card ac-3" role="img" aria-label="Black and white photo of a guitarist"></div>
    <div class="photo artist-card ac-4" role="img" aria-label="Colour photo of a guitarist playing acoustic guitar"></div>
    <div class="abs artist-caption"><b>DARREN HOLT</b><small>GUITARIST</small>
      <span class="go"><svg width="20" height="20" viewBox="0 0 20 20"><path d="M8 6 L12 10 L8 14" fill="none" stroke="#fff" stroke-width="2"/></svg></span>
    </div>
  </section>

  <section>
    <div class="abs news-band"></div>
    <h2 class="abs news-title">NEWS</h2>
    <svg class="abs news-pager" width="44" height="18" viewBox="0 0 44 18"><path d="M14 1 L2 9 L14 17 Z" fill="#fff"/><path d="M28 1 L40 9 L28 17 Z" fill="#fff"/></svg>
    <article class="abs news-body">
      <h3 class="news-headline">Tom Wren&nbsp; Named President &amp; CEO,<br>International,&nbsp; Iron Heron Music production</h3>
      <p class="news-date">London , August 9, 2011</p>
      <p class="news-copy">At vero eos et accusamus et iusto odio dignissimos ducimus qui blanditiis praesentium voluptatum deleniti atque corrupti quos dolores et quas molestias excepturi sint occaecati cupiditate non provident, similique sunt in culpa qui officia deserunt mollitia animi, id est laborum et dolorum fuga. Et harum quidem rerum facilis est et expedita distinctio. Nam libero tempore, cum soluta nobis est eligendi optio cumque nihil impedit quo minus id quod maxime placeat facere possimus, omnis</p>
      <a class="read-more" href="#">READ MORE</a>
    </article>
    <h2 class="abs location-head">LOCATION</h2>
    <div class="photo map" role="img" aria-label="Street map of the studio location in London"></div>
  </section>

  <footer>
    <div class="abs site-footer"></div>
    <div class="abs social"><span></span><span></span><span></span><span></span><span></span></div>
    <nav class="abs footer-nav"><a href="#">HOME</a>|<a href="#">ARTISTS</a>|<a href="#">CONTACT</a></nav>
    <p class="abs copyright">© 2014 IRON-HERON-EXAMPLE.COM</p>
  </footer>

</div>
</body>
</html>
```